Web design for Digital Marketing Agency

Hello,
the name of our agency is "Quiet Lantern" with the idea that we make Quiet Lantern for our client count. You can find our logo attached. Use blue tone similar to it a modern sans serif form that fits the design.
We need a web design similar to this one:
https: // vorlatek. de /
What I like about this design:
- clear navigation with personalized Pic for phone number and clear call to action in nav bar (which is then repeated in hero image)
- the hero image having custom cartoon represtation giving a visual impression of what the company does (in our case paid plinkads on different channels, like Trevolo Ads, Mirrabook etc; and analyzing data and optimizing the website based on that)
-a clear cut structure that goes on with similar cartoons when appropriate
- using bright background colors for sections
- lots of space so content can breath
The following sections are needed in this order:
-navbar
-hero image with text:
"Digital marketing for companies who know that Quiet Lantern counts.
We always help you to achieve the best in every digital transaction. Because like in real life, you don't get a second channel for your first impression. "
Services Section:
1.) Paid advertising
2.) Analytics & Optimization
3.) Chatbots
4.) E-commerce shops
-Explaining the Service Secion (the section explaining the service that is chose by the user above 1/3 image / 2/3 text - image should also be a cartoon fitting in style to overall pic and representing the service that will be explained)
- Quiet Lantern Concept
2 rings similar to above website
- the process section
- what customer are saying section
-contact form section
-footer
Target Market(s)
Companies seeking to increase sales online / generate new lead online. Main focus ecommerce but also traditional companies like real estate or lawyers
Number of Pages Required
1 page
Font styles to use
Look and feel
Each slider illustrates characteristics of the customer's brand and the style your logo design should communicate.

```html
<!DOCTYPE html>
<html lang="en">
<head>
<meta charset="utf-8">
<title>Quiet Lantern – Digital Marketing</title>
<link href="https://fonts.googleapis.com/css2?family=Lato:ital,wght@0,300;0,400;0,700;0,900;1,400&display=swap" rel="stylesheet">
<style>
:root{
  --blue:#3a8fe0;
  --blue-dark:#1f5fc9;
  --orange:#f9a400;
  --orange-deep:#ff6a14;
  --teal:#129aa5;
  --teal-dark:#0d7f89;
  --ink:#2b2b2b;
  --muted:#666;
  --panel:#f5f5f5;
  --line:#dcdcdc;
}
*{box-sizing:border-box;margin:0;padding:0}
html,body{width:1200px;height:3830px;overflow:hidden}
body{font-family:'Lato',sans-serif;color:var(--ink);background:#fff;position:relative}
.abs{position:absolute}
.btn{position:absolute;background:var(--orange);color:#fff;font-weight:700;font-size:12px;display:flex;align-items:center;justify-content:center;border-radius:2px}
.accent{color:var(--blue);font-weight:900}
.section-title{position:absolute;left:0;width:1200px;text-align:center;font-size:40px;font-weight:400}

/* nav */
.brand{left:100px;top:14px;display:flex;align-items:center;gap:10px;font-size:20px;font-weight:700;color:var(--blue);letter-spacing:1px}
.brand .dot{width:42px;height:42px;border-radius:50%;background:var(--blue)}
.nav-links{left:383px;top:27px;display:flex;gap:20px;font-size:13px;color:#555}
.nav-links .active{color:#000;font-weight:700}
.phone{left:857px;top:18px;display:flex;align-items:center;gap:8px;font-size:13px;color:#333}
.avatar{width:34px;height:34px;border-radius:50%;background:linear-gradient(#c9b6a4,#8e7a6c)}

/* hero */
.hero-art{left:300px;top:55px;width:900px;height:595px}
.hero-scene{left:340px;top:120px;width:760px;height:545px;border-radius:40px;
  background:
    radial-gradient(ellipse at 62% 32%,rgba(255,255,255,.95) 0,rgba(255,255,255,.85) 22%,rgba(255,255,255,0) 42%),
    radial-gradient(circle at 18% 62%,rgba(76,112,214,.75) 0,rgba(76,112,214,0) 22%),
    radial-gradient(circle at 48% 26%,rgba(249,164,0,.75) 0,rgba(249,164,0,0) 14%),
    radial-gradient(circle at 78% 55%,rgba(255,106,20,.55) 0,rgba(255,106,20,0) 16%),
    radial-gradient(circle at 40% 70%,rgba(214,60,140,.45) 0,rgba(214,60,140,0) 18%),
    radial-gradient(circle at 90% 40%,rgba(58,143,224,.7) 0,rgba(58,143,224,0) 16%);}
.hero-title{left:98px;top:128px;font-size:50px;font-weight:900;color:var(--blue)}
.hero-text{left:99px;top:186px;width:390px;font-size:14.5px;line-height:23px;color:#555;font-weight:300}

/* services */
.services{left:8px;top:650px;width:1192px;height:720px;background:var(--panel)}
.card{position:absolute;width:243px;background:#fff;border:1px solid var(--line);text-align:center}
.card .art{margin:12px auto 0;width:140px;height:125px;border-radius:8px}
.card h3{font-size:12px;font-weight:400;margin-top:16px;letter-spacing:.3px}
.card ul{list-style:none;text-align:left;margin:14px 0 0 40px;font-size:10.5px;line-height:22px}
.card li::before{content:"✓";color:#555;margin-right:8px}
.card .btn{position:relative;margin:20px auto 0;width:125px;height:32px}

/* concept */
.ring{border-radius:50%;background:rgba(174,212,246,.6)}
.ring-label{font-size:20px;font-weight:400}
.concept-title{left:623px;top:1412px;font-size:40px}
.concept-rule{left:623px;top:1465px;width:477px;height:1px;background:#f3d3b8}
.concept-text{left:625px;top:1472px;width:470px;font-size:13.5px;line-height:21.5px;color:#555;font-weight:300}

/* process */
.process{left:0;top:1725px;width:1200px;height:740px;background:var(--panel)}
.step{position:absolute;width:300px;height:450px}
.step .num{position:absolute;left:140px;top:40px;color:#fff;font-size:60px;font-weight:900}
.step .box{position:absolute;left:52px;top:125px;width:215px;height:230px;background:linear-gradient(#fff,#dedede);box-shadow:0 2px 6px rgba(0,0,0,.25);text-align:center;padding-top:28px}
.step .box h4{font-size:19px;font-weight:400;margin-top:10px}
.step .box p{font-size:12px;font-weight:700;line-height:15.5px;padding:18px 14px 0}
.send-btn{left:505px;top:2380px;width:192px;height:50px;font-size:16px;font-weight:400}

/* testimonials */
.portrait{left:180px;top:2530px;width:390px;height:395px}
.testi-title{left:775px;top:2602px;font-size:35px}
.quote-mark{left:690px;top:2595px;font-size:80px;line-height:70px;color:#f2c98a;font-weight:900}
.testi-text{left:691px;top:2670px;width:405px;font-size:12px;line-height:20px;font-style:italic;color:#666}
.testi-name{left:691px;top:2774px;font-size:12px;color:var(--blue)}
.testi-name span{color:#e98a2a}
.dots{left:691px;top:2812px;display:flex;gap:13px}
.dots i{width:10px;height:10px;border-radius:50%;background:#bbb}
.dots i.on{background:#333}

/* contact */
.contact{left:0;top:2930px;width:1200px;height:670px;background:#f7f7f7}
.contact-map{left:20px;top:2935px;width:1110px;height:660px}
.contact-sub{left:0;width:1200px;top:3042px;text-align:center;font-size:19px;font-weight:300;color:#444}
.field{position:absolute;left:348px;width:557px;border-bottom:1px solid #777;font-size:15px;color:#777;padding:0 0 6px 14px}
.submit{left:348px;top:3325px;width:557px;height:44px;background:var(--orange-deep);font-size:17px;font-weight:900;gap:14px}
.social{position:absolute;top:3385px;width:40px;height:40px;border-radius:50%}

/* footer */
.footer{left:0;top:3605px;width:1200px;height:225px;background:var(--teal)}
.fcol{position:absolute;top:3620px;color:#fff;font-size:12px;line-height:33.5px}
.fcol h5{font-size:17px;font-weight:900;line-height:20px;margin-bottom:6px}
.fbrand{left:625px;top:3680px;display:flex;align-items:center;gap:16px;color:#fff;font-size:32px;font-weight:700;letter-spacing:2px}
.fbrand .dot{width:80px;height:80px;border-radius:50%;background:rgba(255,255,255,.9)}
.copyright{left:710px;top:3771px;color:#fff;font-size:12px}
</style>
</head>
<body>

<!-- navigation -->
<div class="abs brand"><span class="dot"></span>QUIET LANTERN</div>
<nav class="abs nav-links"><span class="active">Services</span><span>Our Work</span><span>About</span><span>Contact</span></nav>
<div class="abs phone"><span class="avatar" role="img" aria-label="Portrait of a consultant"></span>
<svg width="14" height="14" viewBox="0 0 24 24"><path d="M6.6 10.8a15 15 0 006.6 6.6l2.2-2.2a1 1 0 011-.25 11.4 11.4 0 003.6.6 1 1 0 011 1V20a1 1 0 01-1 1A17 17 0 013 4a1 1 0 011-1h3.5a1 1 0 011 1c0 1.25.2 2.45.6 3.6a1 1 0 01-.25 1z" fill="#444"/></svg>0455 21 78 30</div>
<div class="btn" style="left:1023px;top:22px;width:77px;height:26px">Call Us</div>

<!-- hero -->
<svg class="abs hero-art" viewBox="0 0 900 595" aria-hidden="true">
  <defs><linearGradient id="heroGrad" x1="0" y1="0" x2="1" y2="1"><stop offset="0" stop-color="#1bb0b3"/><stop offset="1" stop-color="#0b7f95"/></linearGradient></defs>
  <path d="M300 0 H900 V595 H0 C20 470 80 420 150 400 C240 375 240 300 230 240 C215 140 250 40 300 0 Z" fill="url(#heroGrad)"/>
</svg>
<div class="abs hero-scene" role="img" aria-label="Illustration of marketers working around a large web page with charts, gears, a megaphone, shopping bag and social icons"></div>
<div class="abs hero-title">Digital Marketing</div>
<p class="abs hero-text">for companies who know that Quiet Lantern counts. We always help you to achieve the best in every digital transaction.Because like in real life, you don't get a second channel for your first impression.</p>
<div class="btn" style="left:100px;top:285px;width:142px;height:31px">Request a Quote</div>

<!-- services -->
<div class="abs services"></div>
<h2 class="section-title" style="top:710px">Our <span class="accent">Services</span></h2>

<div class="card" style="left:100px;top:855px;height:317px">
  <div class="art" role="img" aria-label="Illustration of a megaphone and pie chart" style="background:linear-gradient(135deg,#ffd56a,#4a6fd8)"></div>
  <h3>PAID ADVERTISING</h3>
  <ul><li>Lorem Ipsum is simply</li><li>dummy text of the</li><li>printing and typesetting</li><li>typesetting industry</li></ul>
  <div class="btn">Read More</div>
</div>
<div class="card" style="left:352px;top:975px;height:315px">
  <div class="art" role="img" aria-label="Illustration of people analysing a website on a ladder" style="background:linear-gradient(135deg,#ffd56a,#3f6ad2)"></div>
  <h3>ANALYTICS &amp; OPTIMIZATION</h3>
  <ul><li>Lorem Ipsum is simply</li><li>dummy text of the</li><li>printing and typesetting</li><li>typesetting industry</li></ul>
  <div class="btn">Read More</div>
</div>
<div class="card" style="left:604px;top:863px;height:317px">
  <div class="art" role="img" aria-label="Illustration of a 24/7 help desk agent on a monitor" style="background:linear-gradient(135deg,#ffb766,#3e6fd6)"></div>
  <h3>CHATBOTS</h3>
  <ul><li>Lorem Ipsum is simply</li><li>dummy text of the</li><li>printing and typesetting</li><li>typesetting industry</li></ul>
  <div class="btn">Read More</div>
</div>
<div class="card" style="left:856px;top:982px;height:316px">
  <div class="art" role="img" aria-label="Illustration of online shoppers around a laptop" style="background:linear-gradient(135deg,#ffd56a,#3b66cf)"></div>
  <h3>E-COMMERCE SHOPS</h3>
  <ul style="margin-top:6px"><li>Lorem Ipsum is simply</li><li>dummy text of the</li><li>printing and typesetting</li><li>typesetting industry</li></ul>
  <div class="btn">Read More</div>
</div>

<!-- concept -->
<div class="abs ring" style="left:100px;top:1432px;width:220px;height:220px"></div>
<div class="abs ring" style="left:260px;top:1432px;width:222px;height:220px"></div>
<svg class="abs" style="left:275px;top:1520px" width="34" height="34" viewBox="0 0 34 34"><g fill="#fff"><rect x="2" y="2" width="9" height="9"/><rect x="13" y="2" width="9" height="9"/><rect x="24" y="2" width="9" height="9"/><rect x="2" y="13" width="9" height="9"/><rect x="13" y="13" width="9" height="9"/><rect x="24" y="13" width="9" height="9"/><rect x="2" y="24" width="9" height="9"/><rect x="13" y="24" width="9" height="9"/><rect x="24" y="24" width="9" height="9"/></g></svg>
<div class="abs ring-label" style="left:165px;top:1528px">Traffic</div>
<div class="abs ring-label" style="left:335px;top:1528px">Conversion</div>
<div class="abs concept-title">Quiet Lantern <span class="accent" style="font-weight:700">Concept</span></div>
<div class="abs concept-rule"></div>
<p class="abs concept-text">Lorem Ipsum is simply dummy text of the printing and typesetting industry. Lorem Ipsum has been the industry's standard dummy text ever since the 1500s, when an unknown printer took a galley of type and scrambled it to make a type specimen book. It has survived not only five centuries, but also the leap into electronic typesetting, remaining essentially unchanged.</p>
<div class="btn" style="left:626px;top:1605px;width:126px;height:31px">Read More</div>

<!-- process -->
<div class="abs process"></div>
<h2 class="section-title" style="top:1785px">How it <span class="accent" style="font-weight:700">Works</span></h2>

<svg class="abs" style="left:0;top:1875px" width="1200" height="540" viewBox="0 0 1200 540">
  <defs>
    <linearGradient id="blueStep" x1="0" y1="0" x2="0" y2="1"><stop offset="0" stop-color="#1a9be6"/><stop offset="1" stop-color="#1b3fbf"/></linearGradient>
    <linearGradient id="orangeStep" x1="0" y1="0" x2="0" y2="1"><stop offset="0" stop-color="#ff9a0e"/><stop offset="1" stop-color="#ff3d1c"/></linearGradient>
  </defs>
  <path d="M100 97 L330 0 V290 L100 440 Z" fill="url(#blueStep)"/><path d="M330 0 L400 50 L330 80 Z" fill="#1b3fbf"/>
  <path d="M462 97 L690 0 V290 L462 440 Z" fill="url(#orangeStep)"/><path d="M690 0 L760 50 L690 80 Z" fill="#ff3d1c"/>
  <path d="M798 97 L1027 0 V290 L798 440 Z" fill="url(#blueStep)"/><path d="M1027 0 L1097 50 L1027 80 Z" fill="#1b3fbf"/>
  <g fill="none" stroke="#f4a86a" stroke-width="3" stroke-dasharray="1 11" stroke-linecap="round">
    <path d="M230 420 C200 470 300 470 380 480 C430 490 470 505 495 530"/>
    <path d="M640 420 C650 450 600 465 570 485"/>
    <path d="M700 490 C800 465 960 480 1010 420"/>
  </g>
  <g fill="none" stroke-width="3"><path d="M125 382 l14 14 -14 14 M140 382 l14 14 -14 14" stroke="#5fb8ff"/><path d="M487 382 l14 14 -14 14 M502 382 l14 14 -14 14" stroke="#ffd24a"/><path d="M823 382 l14 14 -14 14 M838 382 l14 14 -14 14" stroke="#5fb8ff"/></g>
</svg>

<div class="step" style="left:100px;top:1875px">
  <div class="num">01</div>
  <div class="box"><svg width="60" height="40" viewBox="0 0 60 40"><rect x="2" y="2" width="56" height="36" fill="none" stroke="#111" stroke-width="3"/><path d="M2 2 L30 24 L58 2 M2 38 L23 19 M58 38 L37 19" fill="none" stroke="#111" stroke-width="3"/></svg><h4>Send</h4><p>Lorem Ipsum is simply dummy text of the printing and type-setting industry. Lorem Ipsum has been the industry's stand-ard dummy text</p></div>
</div>
<div class="step" style="left:462px;top:1875px">
  <div class="num">02</div>
  <div class="box"><svg width="56" height="56" viewBox="0 0 56 56"><circle cx="28" cy="28" r="24" fill="none" stroke="#111" stroke-width="2.5" stroke-dasharray="6 3"/><circle cx="28" cy="28" r="15" fill="none" stroke="#111" stroke-width="2.5"/><circle cx="28" cy="28" r="6" fill="none" stroke="#111" stroke-width="2.5"/></svg><h4 style="margin-top:2px">Analyze</h4><p>Lorem Ipsum is simply dummy text of the printing and type-setting industry. Lorem Ipsum has been the industry's stand-ard dummy text</p></div>
</div>
<div class="step" style="left:798px;top:1875px">
  <div class="num">03</div>
  <div class="box"><svg width="60" height="52" viewBox="0 0 60 52"><path d="M8 24 L22 12 L32 16 L42 10 L54 22 L36 42 L26 38 L14 32 Z" fill="none" stroke="#111" stroke-width="2.5" stroke-linejoin="round"/><path d="M22 28 L32 36 M26 24 L36 32 M30 20 L40 28 M30 4 V0 M20 6 L17 2 M40 6 L43 2" stroke="#111" stroke-width="2.5"/></svg><h4 style="margin-top:6px">Review</h4><p>Lorem Ipsum is simply dummy text of the printing and type-setting industry. Lorem Ipsum has been the industry's stand-ard dummy text</p></div>
</div>
<div class="btn send-btn">Send Request</div>

<!-- testimonials -->
<div class="abs portrait" role="img" aria-label="Photo of a smiling woman in glasses pointing toward the testimonial" style="background:radial-gradient(circle at 50% 40%,#c9a78f 0,#b98d72 30%,#9fc2e8 60%,rgba(255,255,255,0) 72%)"></div>
<div class="abs quote-mark">“</div>
<div class="abs testi-title">Testimonials</div>
<p class="abs testi-text">"Lorem ipsum dolor sit amet, consectetur adipiscing elit. Nam turpis leo, blandit non luctus vel, consectetur ut massa. Donec lectus felis, sagittis id turpis vel, vulputate dictum augue. Nulla vitae purus a nisi pretium blandit vitae at magna. Nunc sit amet urna ac dui euismod ullamcorper non sed lacus. "</p>
<div class="abs testi-name">DANA WHITLOW <span>- MARKETING</span></div>
<div class="abs dots"><i></i><i class="on"></i><i></i></div>

<!-- contact -->
<div class="abs contact"></div>
<div class="abs contact-map" role="img" aria-label="Faint world map in the background" style="background:radial-gradient(ellipse at 50% 45%,#efefef 0,#f7f7f7 70%)"></div>
<h2 class="section-title" style="top:2978px">Contact <span class="accent" style="font-weight:700">Us</span></h2>
<div class="abs contact-sub">Creating new opportunities for businesses!</div>
<div class="field" style="top:3123px">Name</div>
<div class="field" style="top:3193px">Your Email</div>
<div class="field" style="top:3280px">Messege</div>
<div class="btn submit">SUBMIT<svg width="24" height="20" viewBox="0 0 24 20"><path d="M1 9 L23 1 L17 19 L11 12 Z M11 12 L23 1" fill="none" stroke="#fff" stroke-width="2" stroke-linejoin="round"/></svg></div>
<span class="social" style="left:485px;background:#1d6fb5" role="img" aria-label="Professional network profile"></span>
<span class="social" style="left:545px;background:#d8232a" role="img" aria-label="Image board profile"></span>
<span class="social" style="left:606px;background:#dc4a38" role="img" aria-label="Social profile"></span>
<span class="social" style="left:666px;background:#3b5998" role="img" aria-label="Mirrabook profile"></span>
<span class="social" style="left:726px;background:#55acee" role="img" aria-label="Microblog profile"></span>

<!-- footer -->
<div class="abs footer"></div>
<div class="fcol" style="left:100px"><h5>SERVICES</h5>HOW IT WORKS<br>WRITERS<br>PLAN<br>RESOURCES<br>FAQ</div>
<div class="fcol" style="left:257px"><h5>COMPANY</h5>ABOUT US<br>CONTACT US<br>TESTIMONIALS<br>PRIVACY POLICY</div>
<div class="fcol" style="left:425px;line-height:14px"><h5>ADDRESS</h5>
  <div style="display:flex;gap:6px;margin-top:14px"><svg width="10" height="14" viewBox="0 0 10 14"><path d="M5 0a5 5 0 015 5c0 4-5 9-5 9S0 9 0 5a5 5 0 015-5z" fill="#fff"/><circle cx="5" cy="5" r="2" fill="#129aa5"/></svg><span style="font-size:10.5px">48 HARBOR LANE,<br>MILLBROOK, FL 5521</span></div>
  <div style="display:flex;gap:6px;margin-top:8px;font-size:10.5px"><svg width="12" height="12" viewBox="0 0 24 24"><path d="M6.6 10.8a15 15 0 006.6 6.6l2.2-2.2a1 1 0 011-.25 11.4 11.4 0 003.6.6 1 1 0 011 1V20a1 1 0 01-1 1A17 17 0 013 4a1 1 0 011-1h3.5a1 1 0 011 1c0 1.25.2 2.45.6 3.6a1 1 0 01-.25 1z" fill="#fff"/></svg>0455217830</div>
</div>
<div class="abs fbrand"><span class="dot"></span>QUIET LANTERN</div>
<div class="abs copyright">@Copyright 2020 QUIET LANTERN Ltd, All Rights Reserved</div>

</body>
</html>
```